Modern business card design for professional copywriter

I'd like a business card design that I can use to have my cards printed out by plink.com as a squared corners business card (see artwork and design guidelines here: https://help.plink.com/hc/en-gb/sections/300481726-PLINK-Product-Templates)

The design should be clean and modern and reflect the colours, tone and branding on my website: https://noravestrel.com.au

Target Market(s)

Professionals, B2B small business owners

Industry/Entity Type

Business

Contact Information for Business Card

Nora Vestrel
m: 0427 593 864
e: nora@noravestrel.com.au
w: noravestrel.com.au

Font styles to use
Sans Serif

Requirements
Must have
• Tagline: "Smart copywriting for clever business people"
• Brand colours: fd8000, 009984, 666666 and black
Nice to have

```html
<!DOCTYPE html>
<html lang="en">
<head>
<meta charset="utf-8">
<title>Nora Vestrel – Business Card</title>
<link rel="stylesheet" href="https://fonts.googleapis.com/css2?family=Open+Sans:wght@400;600&display=swap">
<style>
  :root {
    --paper: #ffffff;
    --brand-orange: #fd6a1e;
    --brand-green: #2ecc71;
    --brand-grey: #555a5c;
    --green-light: #1fd17a;
    --green-dark: #13905a;
    --orange-light: #e08a55;
    --orange-mid: #d2692a;
    --orange-deep: #a8460f;
    --orange-shadow: #5a2608;
    --ink-light: #ffffff;
  }
  * { margin: 0; padding: 0; box-sizing: border-box; }
  html, body {
    width: 805px;
    height: 1200px;
    overflow: hidden;
    background: var(--paper);
  }
  .card {
    position: relative;
    width: 805px;
    height: 1200px;
    background: var(--paper);
    font-family: "Open Sans", "Verdana", sans-serif;
    overflow: hidden;
  }
  .card-art {
    position: absolute;
    inset: 0;
    width: 805px;
    height: 1200px;
  }
  .brand {
    position: absolute;
    left: 60px;
    top: 168px;
    width: 690px;
    display: flex;
    flex-direction: column;
    align-items: flex-end;
  }
  .brand-row {
    display: flex;
    align-items: center;
    gap: 24px;
  }
  .brand-square {
    width: 50px;
    height: 50px;
    background: var(--brand-green);
  }
  .brand-name {
    font-size: 104px;
    font-weight: 600;
    color: var(--brand-orange);
    letter-spacing: -1px;
    line-height: 1;
  }
  .brand-tagline {
    margin-top: 10px;
    font-size: 21px;
    font-weight: 400;
    color: var(--brand-grey);
    letter-spacing: 1px;
    line-height: 1.2;
  }
  .contact {
    position: absolute;
    left: 80px;
    top: 720px;
    color: var(--ink-light);
  }
  .contact-name {
    font-size: 50px;
    font-weight: 400;
    margin-left: 105px;
    line-height: 1;
    margin-bottom: 44px;
    letter-spacing: 1px;
  }
  .contact-list { list-style: none; }
  .contact-item {
    display: flex;
    align-items: center;
    height: 110px;
  }
  .contact-icon {
    width: 85px;
    height: 80px;
    margin-right: 20px;
    flex: none;
  }
  .contact-phone { font-size: 46px; letter-spacing: 2px; }
  .contact-email { font-size: 39px; }
  .contact-web { font-size: 41px; }
</style>
</head>
<body>
<div class="card">
  <svg class="card-art" viewBox="0 0 805 1200" xmlns="http://www.w3.org/2000/svg">
    <defs>
      <linearGradient id="greenFacets" x1="0" y1="0" x2="1" y2="0">
        <stop offset="0" stop-color="var(--green-light)"/>
        <stop offset="0.5" stop-color="var(--green-dark)"/>
        <stop offset="1" stop-color="var(--green-light)"/>
      </linearGradient>
      <linearGradient id="orangeFacets" x1="0" y1="0" x2="1" y2="1">
        <stop offset="0" stop-color="var(--orange-light)"/>
        <stop offset="0.45" stop-color="var(--orange-mid)"/>
        <stop offset="0.85" stop-color="var(--orange-deep)"/>
        <stop offset="1" stop-color="var(--orange-shadow)"/>
      </linearGradient>
    </defs>
    <polygon class="top-facets" role="img" aria-label="Green low-poly faceted pattern"
      fill="url(#greenFacets)"
      points="104,0 805,0 805,110 712,30 602,115 390,88 182,115"/>
    <polygon class="lower-facets" role="img" aria-label="Orange low-poly faceted pattern"
      fill="url(#orangeFacets)"
      points="0,335 341,398 578,335 762,398 805,346 805,1200 0,1200"/>
    <rect class="contact-band" x="0" y="681" width="805" height="485" fill="rgba(110,40,0,0.12)"/>
  </svg>

  <div class="brand">
    <div class="brand-row">
      <div class="brand-square"></div>
      <div class="brand-name">Nora Vestrel</div>
    </div>
    <p class="brand-tagline">Smart copywriting for clever business people</p>
  </div>

  <div class="contact">
    <p class="contact-name">Nora Vestrel</p>
    <ul class="contact-list">
      <li class="contact-item">
        <svg class="contact-icon" viewBox="0 0 85 80" aria-hidden="true">
          <rect x="22" y="2" width="38" height="74" rx="7" fill="none" stroke="#fff" stroke-width="6"/>
          <circle cx="41" cy="68" r="3" fill="#fff"/>
        </svg>
        <span class="contact-phone">0427 593 864</span>
      </li>
      <li class="contact-item">
        <svg class="contact-icon" viewBox="0 0 85 80" aria-hidden="true">
          <rect x="2" y="18" width="80" height="52" fill="#fff"/>
          <polyline points="2,18 42,50 82,18" fill="none" stroke="var(--orange-mid)" stroke-width="5"/>
          <line x1="2" y1="70" x2="32" y2="42" stroke="var(--orange-mid)" stroke-width="4"/>
          <line x1="82" y1="70" x2="52" y2="42" stroke="var(--orange-mid)" stroke-width="4"/>
        </svg>
        <span class="contact-email">nora@noravestrel.com.au</span>
      </li>
      <li class="contact-item">
        <svg class="contact-icon" viewBox="0 0 85 80" aria-hidden="true">
          <g fill="none" stroke="#fff" stroke-width="5">
            <circle cx="38" cy="38" r="32"/>
            <ellipse cx="38" cy="38" rx="14" ry="32"/>
            <line x1="6" y1="38" x2="70" y2="38"/>
            <line x1="38" y1="6" x2="38" y2="70"/>
            <path d="M12 20 H64 M12 56 H64"/>
          </g>
          <polygon points="50,44 80,58 66,62 74,76 68,79 60,65 50,74" fill="#fff" stroke="var(--orange-mid)" stroke-width="3"/>
        </svg>
        <span class="contact-web">noravestrel.com.au</span>
      </li>
    </ul>
  </div>
</div>
</body>
</html>
```